Corvid Lens Studio Business Card Design

I need a business card designed for a photography business based in Perth, Western Australia called Corvid Lens Studio.

We specialise in wedding, event photography and portrait photography.

The business card must borrow the style of the attached logo.

The hex codes for the colours in the logo are:
#ED1D85 - Pink
#89C23E - Green
#37282F - Black

The name on the card will be:
Name: Tobiah
Phone: 0417395268
Website: www.corvidlensstudio.com.au
Social: corvidlensstudio

I am open and happy to accept creative concepts.

Industry/Entity Type

Business

```html
<!DOCTYPE html>
<html lang="en">
<head>
<meta charset="utf-8">
<title>Corvid Lens Studio – Business Card</title>
<link rel="stylesheet" href="https://fonts.googleapis.com/css2?family=Questrial&display=swap">
<style>
  :root {
    --pink: #ED1D85;
    --pink-soft: #F07AAE;
    --green: #89C23E;
    --ink: #37282F;
    --ink-soft: #5a5054;
    --card: #ffffff;
    --backdrop: #ececec;
  }
  * { margin: 0; padding: 0; box-sizing: border-box; }
  html, body {
    width: 1200px;
    height: 720px;
    overflow: hidden;
    background: var(--backdrop);
    font-family: "Questrial", "Helvetica Neue", Arial, sans-serif;
  }
  .canvas {
    position: relative;
    width: 1200px;
    height: 720px;
  }
  .card {
    position: absolute;
    top: 210px;
    width: 520px;
    height: 300px;
    background: var(--card);
    box-shadow: 0 2px 3px rgba(0,0,0,0.06), 0 12px 30px rgba(0,0,0,0.08);
  }
  .card--front { left: 50px; }
  .card--back { left: 630px; }

  /* Front */
  .brand {
    position: absolute;
    inset: 0;
    display: flex;
    flex-direction: column;
    align-items: center;
    justify-content: center;
    gap: 30px;
  }
  .brand__dot {
    width: 110px;
    height: 110px;
    border-radius: 50%;
    background: var(--pink-soft);
  }
  .brand__name {
    color: var(--ink-soft);
    font-size: 17px;
    letter-spacing: 0.42em;
    text-transform: uppercase;
    padding-left: 0.42em;
  }

  /* Back */
  .contact {
    position: absolute;
    left: 44px;
    bottom: 40px;
    color: var(--ink-soft);
  }
  .contact__name {
    font-size: 42px;
    letter-spacing: 0.12em;
    text-transform: uppercase;
    color: var(--ink);
    margin-bottom: 26px;
  }
  .contact__line {
    font-size: 14px;
    letter-spacing: 0.14em;
    text-transform: uppercase;
    line-height: 1.9;
  }
  .contact__accent {
    position: absolute;
    top: 34px;
    right: 34px;
    width: 14px;
    height: 14px;
    border-radius: 50%;
    background: var(--pink);
  }
</style>
</head>
<body>
  <main class="canvas">
    <section class="card card--front" aria-label="Card front">
      <div class="brand">
        <span class="brand__dot" aria-hidden="true"></span>
        <p class="brand__name">Corvid Lens Studio</p>
      </div>
    </section>

    <section class="card card--back" aria-label="Card back">
      <span class="contact__accent" aria-hidden="true"></span>
      <div class="contact">
        <h1 class="contact__name">Tobiah</h1>
        <p class="contact__line">Phone: 0417395268</p>
        <p class="contact__line">www.corvidlensstudio.com.au</p>
        <p class="contact__line">Social: corvidlensstudio</p>
      </div>
    </section>
  </main>
</body>
</html>
```